Elegant, Playful, Health And Wellness Packaging Design for an Essential Oil Diffuser

Box design for diffuser, should be elegant, luxury, white box with gold foil and vibrant color combination that pops off the white box.

Designs look the same

```html
<!DOCTYPE html>
<html lang="en">
<head>
<meta charset="utf-8">
<title>LUMERA AURI Ultrasonic Diffuser Packaging</title>
<link href="https://fonts.googleapis.com/css2?family=Cinzel:wght@500;700&family=Montserrat:wght@400;500;600&display=swap" rel="stylesheet">
<style>
  :root{
    --gold:#b8862f;
    --gold-light:#d8b46a;
    --navy:#1c2230;
    --white:#ffffff;
    --paper:#f7f7f5;
    --silver:#dcdde0;
    --ink:#3a3a3a;
  }
  *{margin:0;padding:0;box-sizing:border-box}
  html,body{width:720px;height:1200px;overflow:hidden;background:var(--white)}
  body{position:relative;font-family:'Montserrat',sans-serif;color:var(--ink)}

  .dieline-stage{position:absolute;left:0;top:0;width:720px;height:600px;background:var(--gold)}
  .dieline-shapes{position:absolute;left:0;top:0}
  .panel{position:absolute;background:var(--white);overflow:hidden}
  .panel-band{position:absolute;left:0;right:0;bottom:0;height:14px;background:var(--navy);border-top:3px solid var(--gold-light)}
  .info-block{position:absolute;left:8px;right:8px;top:14px;background:var(--gold);color:var(--white);padding:8px;font-size:7px;line-height:1.4;font-weight:500}
  .info-block strong{display:block;font-size:8px;font-weight:600;margin-bottom:2px}
  .feature-list{position:absolute;left:10px;right:8px;top:16px;list-style:none;font-size:6.5px;line-height:1.9;color:var(--ink)}
  .feature-list li::before{content:"";display:inline-block;width:4px;height:4px;background:var(--gold);border-radius:50%;margin-right:4px;vertical-align:middle}
  .panel-title{position:absolute;left:10px;top:8px;font-size:6px;letter-spacing:1px;color:var(--gold);font-weight:600}

  .top-flap{position:absolute;left:264px;top:50px;width:144px;height:130px;background:var(--navy);border-radius:14px 14px 0 0;display:flex;align-items:center;justify-content:center;gap:6px}
  .top-flap .brand-name{font-size:13px}

  .brand{display:flex;align-items:center;justify-content:center;gap:8px}
  .brand-dot{width:18px;height:18px;border-radius:50%;background:var(--gold-light)}
  .brand-name{font-family:'Montserrat',sans-serif;font-weight:600;letter-spacing:4px;color:var(--gold-light);font-size:26px}

  .front-panel{position:absolute;width:380px;height:430px;background:var(--white);overflow:hidden}
  .front-panel .header{position:absolute;left:0;top:0;width:100%;height:118px;background:var(--navy);border-bottom:4px solid var(--gold)}
  .front-panel .header .brand{height:100%;flex-direction:column;gap:10px}
  .front-panel .tagline{position:absolute;top:130px;width:100%;text-align:center;font-size:10px;letter-spacing:2px;color:var(--gold);font-weight:500}
  .front-panel .product-art{position:absolute;left:40px;top:158px;width:300px;height:196px;border-radius:60px 60px 30px 30px;background:radial-gradient(ellipse at 50% 40%,#ffffff 0%,#eceded 55%,var(--silver) 100%)}
  .front-panel .product-name{position:absolute;top:205px;width:100%;text-align:center;font-family:'Cinzel',serif;font-weight:700;font-size:72px;color:#4a4d55;letter-spacing:4px}
  .front-panel .name-bar{position:absolute;left:110px;top:298px;width:160px;height:8px;background:var(--gold-light)}
  .front-panel .footer{position:absolute;left:0;bottom:0;width:100%;height:62px;background:var(--gold);border-top:12px solid var(--navy)}
  .front-panel .footer-text{position:absolute;width:100%;top:14px;text-align:center;font-size:10px;letter-spacing:3px;color:var(--white);font-weight:600}

  .dieline-front{position:absolute;left:264px;top:180px;width:144px;height:170px;overflow:hidden}
  .dieline-front .front-panel{transform:scale(.379,.395);transform-origin:0 0}

  .flat-front{left:170px;top:650px;box-shadow:0 0 0 1px #e4e4e4}
  .caption{position:absolute;left:150px;top:1120px;width:420px;text-align:center;font-size:8.5px;line-height:1.5;color:#555}
</style>
</head>
<body>

<section class="dieline-stage" aria-label="Box dieline">
  <svg class="dieline-shapes" width="720" height="600" aria-hidden="true">
    <polygon points="150,350 264,350 250,470 164,470" fill="#fff"/>
    <polygon points="264,350 408,350 400,500 272,500" fill="#fff"/>
    <polygon points="408,350 520,350 506,470 422,470" fill="#fff"/>
    <polygon points="520,350 670,350 660,380 600,500 560,500 530,380" fill="#fff"/>
    <polygon points="50,350 150,350 140,380 70,380" fill="#fff"/>
    <polygon points="150,180 264,180 250,150 164,150" fill="#fff"/>
    <polygon points="408,180 520,180 506,150 422,150" fill="#fff"/>
    <rect x="272" y="470" width="128" height="12" fill="#1c2230"/>
  </svg>

  <div class="top-flap"><span class="brand-dot"></span><span class="brand-name">LUMERA</span></div>

  <div class="panel" style="left:50px;top:180px;width:100px;height:170px">
    <div class="info-block"><strong>Ultrasonic Aroma Diffuser</strong>300 ml Capacity</div>
    <div class="panel-band"></div>
  </div>
  <div class="panel" style="left:150px;top:180px;width:114px;height:170px">
    <ul class="feature-list">
      <li>Whisper-quiet mist</li><li>Seven soft colours</li><li>Auto shut-off</li><li>Timer settings</li><li>Easy to clean</li>
    </ul>
    <div class="panel-band"></div>
  </div>

  <div class="dieline-front">
    <div class="front-panel">
      <div class="header"><div class="brand"><span class="brand-dot"></span><span class="brand-name">LUMERA</span></div></div>
      <p class="tagline">EXPERIENCE THE ESSENCE OF NATURE</p>
      <div class="product-art" role="img" aria-label="White ultrasonic diffuser with soft mist waves"></div>
      <p class="product-name">AURI</p>
      <div class="name-bar"></div>
      <div class="footer"><p class="footer-text">ULTRASONIC DIFFUSER</p></div>
    </div>
  </div>

  <div class="panel" style="left:408px;top:180px;width:112px;height:170px">
    <p class="panel-title">FEATURES</p>
    <ul class="feature-list" style="top:22px">
      <li>Whisper-quiet mist</li><li>Seven soft colours</li><li>Auto shut-off</li><li>Timer settings</li><li>Easy to clean</li>
    </ul>
    <div class="panel-band"></div>
  </div>
  <div class="panel" style="left:520px;top:180px;width:150px;height:170px">
    <div class="info-block"><strong>Your Oils at Home</strong>Fill, add drops, relax.</div>
    <div class="panel-band"></div>
  </div>
</section>

<div class="front-panel flat-front">
  <div class="header"><div class="brand"><span class="brand-dot"></span><span class="brand-name">LUMERA</span></div></div>
  <p class="tagline">EXPERIENCE THE ESSENCE OF NATURE</p>
  <div class="product-art" role="img" aria-label="White ultrasonic diffuser with soft mist waves"></div>
  <p class="product-name">AURI</p>
  <div class="name-bar"></div>
  <div class="footer"><p class="footer-text">ULTRASONIC DIFFUSER</p></div>
</div>

<p class="caption">Lorem ipsum dolor sit amet, consectetur adipiscing elit, sed do eiusmod tempor incididunt ut labore et dolore magna aliqua. Ut enim ad minim veniam, quis nostrud exercitation ullamco laboris nisi ut aliquip ex ea commodo consequat. Duis aute irure dolor in reprehenderit in voluptate velit esse cillum dolore eu fugiat nulla pariatur.</p>

</body>
</html>
```